Project Lists Banner for HVAC ecommerce store

We want a banner that showcases our project list feature that will allow customers to create list of products that they can select and quickly order. this will be a middle of page banner. It will replace this banner - https://www.glimmerpanecapture.com/image/48305712
Font: Noto Sans
Size: 938x300 px
Color Options: #0059E, #00BBE3, #C6C8C7
Text:
Create lists of frequently purchased SKU's for fast ordering.
- Warehouse Inventory
- Complete Systems
- Large Projects
- And More...
"Sign In" is the call to action button. make button with non rounded (square) boarders.
We don't want a computer screen in banner nor a person. You can look at our competitors below for ideas.
Our staging server is plumvale7.com for reference
Our competitors:
https://www.brightfolddepot.com/
https://www.tolvexa.com/
https://www.plosk.com/
https://www.vimbo.com/index.html
HVAC, B2B
HVAC

```html
<!DOCTYPE html>
<html lang="en">
<head>
<meta charset="utf-8">
<title>Project Lists Banner</title>
<link rel="stylesheet" href="https://fonts.googleapis.com/css2?family=Noto+Sans:wght@300;400;600;700;800&display=swap">
<style>
  :root {
    --cyan: #00BBE3;
    --blue: #1d5aa8;
    --blue-light: #9fbde3;
    --grey: #C6C8C7;
    --ink: #2e3030;
    --ink-soft: #3a3c3c;
    --line: #dcdfe2;
    --ui-text: #555b60;
    --white: #ffffff;
  }
  * { box-sizing: border-box; margin: 0; padding: 0; }
  html, body { width: 1200px; height: 626px; overflow: hidden; background: var(--white); }
  body { font-family: "Noto Sans", sans-serif; }

  .stage { width: 1219px; height: 635px; transform: scale(0.9844); transform-origin: 0 0; position: relative; }

  .banner { position: absolute; left: 141px; top: 168px; width: 938px; height: 300px; overflow: hidden; background: var(--white); }

  /* project list interface backdrop */
  .ui { position: absolute; inset: 0; font-size: 6px; color: var(--ui-text); }
  .ui-box { position: absolute; background: var(--white); border: 1px solid var(--line); }
  .account-menu { left: 4px; top: 30px; width: 114px; height: 130px; padding: 8px 7px; }
  .account-menu li { list-style: none; text-transform: uppercase; font-size: 5.5px; line-height: 11.4px; color: #555; }
  .account-menu li.is-active { color: var(--blue); }
  .import-panel { left: 4px; top: 168px; width: 114px; height: 115px; padding: 8px 7px; }
  .import-title { font-weight: 700; font-size: 6.5px; color: #333; display: flex; gap: 4px; align-items: center; }
  .import-title i { width: 8px; height: 7px; border: 1px solid #333; display: block; }
  .drop-zone { margin-top: 7px; border: 1px dashed #777; height: 64px; text-align: center; padding: 5px 4px; font-size: 5.2px; line-height: 7px; }
  .choose-btn { display: block; margin: 3px auto 0; width: 60px; height: 12px; background: #1b4f95; color: var(--white); font-weight: 700; line-height: 12px; }
  .sample-link { display: block; margin-top: 5px; color: var(--blue); text-decoration: underline; }
  .tutorial-btn { margin: 8px auto 0; width: 60px; height: 12px; background: #f07c2a; color: var(--white); text-align: center; line-height: 12px; font-weight: 600; }

  .page-title { position: absolute; left: 126px; top: 10px; font-size: 8px; color: #bbb; }
  .project-bar { position: absolute; left: 125px; top: 41px; width: 470px; height: 15px; background: linear-gradient(90deg, var(--blue), #8fb0da); color: var(--white); font-weight: 700; font-size: 7.5px; padding-left: 7px; line-height: 15px; }
  .project-card { left: 125px; top: 56px; width: 470px; height: 80px; border-top: 0; }
  .field { position: absolute; border: 1px solid var(--line); background: var(--white); font-size: 5.5px; padding-left: 5px; line-height: 16px; height: 18px; }
  .field-select { left: 133px; top: 64px; width: 230px; }
  .field-name { left: 133px; top: 104px; width: 230px; }
  .field-notes { left: 368px; top: 104px; width: 240px; height: 26px; }
  .add-field { left: 125px; top: 147px; width: 160px; }
  .add-btn { position: absolute; left: 288px; top: 147px; width: 48px; height: 18px; background: var(--blue-light); color: var(--white); font-weight: 700; font-size: 6px; text-align: center; line-height: 18px; }

  .sku-table { position: absolute; left: 125px; top: 182px; width: 560px; }
  .sku-head, .sku-row { position: relative; height: 25px; border-bottom: 1px solid var(--line); }
  .sku-head { height: 18px; background: #f1f2f3; font-weight: 700; font-size: 5.5px; line-height: 18px; }
  .check { position: absolute; left: 8px; top: 50%; width: 7px; height: 7px; margin-top: -3.5px; border: 1px solid #999; background: var(--white); }
  .sku-head .label { position: absolute; left: 24px; }
  .sku-head .qty { position: absolute; left: 330px; }
  .sku-head .price { position: absolute; left: 370px; }
  .brand { position: absolute; left: 23px; top: 9px; font-size: 4.5px; font-weight: 700; color: #555; }
  .item { position: absolute; left: 47px; top: 5px; font-size: 5.3px; line-height: 7px; }
  .item b { color: #555; }
  .stepper { position: absolute; left: 302px; top: 4px; display: flex; }
  .stepper span { width: 16px; height: 16px; border: 1px solid #c6c6c6; background: #777; color: var(--white); text-align: center; line-height: 15px; }
  .stepper span.count { width: 22px; background: var(--white); color: #555; }
  .unit { position: absolute; left: 370px; top: 9px; }

  /* grey wash */
  .wash { position: absolute; inset: 0; background: linear-gradient(90deg, rgba(255,255,255,0.45) 0%, rgba(255,255,255,0.3) 32%, rgba(210,212,211,0.75) 48%, rgba(198,200,199,0.95) 62%, var(--grey) 100%); }

  .bands { position: absolute; inset: 0; }

  /* message */
  .headline { position: absolute; left: 411px; top: 30px; font-weight: 800; font-size: 28.5px; line-height: 40px; color: var(--ink); letter-spacing: -0.1px; }
  .uses { list-style: none; }
  .uses li { position: absolute; font-weight: 400; font-size: 21px; color: var(--ink-soft); white-space: nowrap; }
  .sign-in { position: absolute; left: 821px; top: 245px; width: 82px; height: 22px; background: var(--cyan); color: #173042; font-weight: 700; font-size: 11.5px; text-align: center; line-height: 22px; text-decoration: none; border-radius: 0; }
</style>
</head>
<body>
<div class="stage">
  <section class="banner">
    <div class="ui" aria-hidden="true">
      <p class="page-title">My Project Lists</p>
      <ul class="ui-box account-menu">
        <li>Dashboard</li><li>Profile</li><li>Address Book</li><li>Manage Users</li><li>Invoice History</li><li>Order History</li><li>Statements</li><li>My Quotes</li><li>Favorites</li><li class="is-active">Project Lists</li>
      </ul>
      <div class="ui-box import-panel">
        <p class="import-title"><i></i>Import Project Lists</p>
        <div class="drop-zone">Drag and drop a .CSV file here, or select file from your computer.
          <span class="choose-btn">Choose File</span>
          <span class="sample-link">Download Sample CSV</span>
        </div>
        <div class="tutorial-btn">Tutorial</div>
      </div>
      <div class="project-bar">Project:</div>
      <div class="ui-box project-card"></div>
      <div class="field field-select">Main</div>
      <div class="field field-name">Main</div>
      <div class="field field-notes"></div>
      <div class="field add-field">Enter Product Name or SKU to Add</div>
      <div class="add-btn">Add to List</div>
      <div class="sku-table">
        <div class="sku-head"><span class="check"></span><span class="label">Product/SKU</span><span class="qty">Qty</span><span class="price">Sell Price</span></div>
        <div class="sku-row"><span class="check"></span><span class="brand">NORVIK</span><p class="item"><b>Hail Guard 6.5/12.5 Ranger</b><br>1HG0411</p><div class="stepper"><span>−</span><span class="count">1</span><span>+</span></div><span class="unit">$47.50</span></div>
        <div class="sku-row"><span class="check"></span><span class="brand">NORVIK</span><p class="item"><b>Screwdriver, Combo, 6-In-1</b><br>DIV-S-61</p><div class="stepper"><span>−</span><span class="count">6</span><span>+</span></div><span class="unit">$5.95</span></div>
        <div class="sku-row"><span class="check"></span><span class="brand">NORVIK</span><p class="item"><b>Hand Seamer, Talvo</b><br>DIV-S40-FCTMS1</p><div class="stepper"><span>−</span><span class="count">10</span><span>+</span></div><span class="unit">$30.00</span></div>
        <div class="sku-row"><span class="check"></span><span class="brand">NORVIK</span><p class="item"><b>Condenser Mounting Brackets, 1/8" Steel, 600Lb Per Pair</b><br>DIV-ACB-42</p><div class="stepper"><span>−</span><span class="count">1</span><span>+</span></div><span class="unit">$22.00</span></div>
      </div>
    </div>

    <div class="wash"></div>

    <svg class="bands" width="938" height="300" viewBox="0 0 938 300" aria-hidden="true">
      <polygon points="0,0 938,0 938,3 0,22" fill="var(--cyan)"/>
      <polygon points="0,290 938,277 938,300 0,300" fill="var(--cyan)"/>
    </svg>

    <h2 class="headline">Create lists of frequently<br>purchased SKU's for fast ordering.</h2>
    <ul class="uses">
      <li style="left:469px; top:128px;">Warehouse Inventory</li>
      <li style="left:529px; top:165px;">Complete Systems</li>
      <li style="left:606px; top:202px;">Large Projects</li>
      <li style="left:671px; top:238px;">And More...</li>
    </ul>
    <a class="sign-in" href="#">SIGN IN</a>
  </section>
</div>
</body>
</html>
```